R. T. HOLLOWAY, INC. is a US based Investment firm looking for a five-page website design.

Currently, their temporary site is located at: rtholloway.com and they would like to maintain the site design as much as possible.

R. T. HOLLOWAY, INC. sister companies are: Crestvale Lodge Investments (c-lodge.com) Benwick Petroleum (benwick-petroleum.com) and RTHF (rth-foundation.org/en)

Attached is a .ZIP file with designs and assets we think will be useful for your proposal… Content for the site is attached on: rtholloway website content.docx Current temp website design is attached as: Coming Soon Website.zip .EPS Logo files attached as: rtholloway logos.zip Sample business card attached as: R T Holloway Business cards.eps Other assets, such as Fonts and background images attached as: Assets.zip

Target Market(s)

Investors

Industry/Entity Type

Investments

Number of Pages Required

5+ page

Requirements
Must have
• Contact Page with a form.

```html
<!DOCTYPE html>
<html lang="en">
<head>
<meta charset="utf-8">
<title>R. T. Holloway, Inc.</title>
<link href="https://fonts.googleapis.com/css2?family=Cinzel:wght@400;600;700&family=Open+Sans:wght@400;600;700&display=swap" rel="stylesheet">
<style>
:root{
  --gold:#b3955a;
  --gold-dark:#9a7d45;
  --gold-soft:#e9dfc9;
  --navy:#1f2a3a;
  --navy-deep:#18212f;
  --ink:#2b2b2b;
  --muted:#6d6d6d;
  --line:#e3e3e3;
  --white:#ffffff;
}
*{box-sizing:border-box;margin:0;padding:0}
html,body{width:1200px;height:3860px;overflow:hidden}
body{background:var(--white);font-family:"Open Sans",Arial,sans-serif;color:var(--ink);position:relative}
.serif{font-family:"Cinzel",Georgia,serif}

/* header */
.site-header{position:absolute;top:0;left:0;width:1200px;height:90px;display:flex;align-items:center;padding:0 110px 0 120px}
.brand{display:flex;align-items:center;gap:10px}
.brand-dot{width:34px;height:34px;border-radius:50%;border:2px solid var(--gold)}
.brand-name{font-family:"Cinzel",Georgia,serif;font-size:15px;font-weight:600;color:var(--gold);letter-spacing:1px}
.main-nav{display:flex;gap:26px;margin-left:220px}
.main-nav a{font-size:11px;font-weight:600;color:var(--ink);text-decoration:none;letter-spacing:.6px;padding:8px 10px}
.main-nav a.is-active{border:1px solid var(--gold);border-radius:14px;color:var(--gold)}
.call{margin-left:auto;display:flex;align-items:center;gap:10px}
.call-icon{width:32px;height:32px;border-radius:50%;background:var(--gold);display:flex;align-items:center;justify-content:center}
.call small{display:block;font-size:10px;color:var(--muted)}
.call strong{font-size:14px;color:var(--ink)}

/* hero */
.hero{position:absolute;top:90px;left:0;width:1200px;height:630px}
.hero h1{position:absolute;left:60px;top:100px;font-family:"Cinzel",Georgia,serif;font-size:42px;font-weight:600;color:var(--navy);letter-spacing:1px}
.hero p{position:absolute;left:60px;top:158px;font-size:14px;color:var(--muted)}
.btn{display:inline-flex;align-items:center;gap:12px;background:var(--gold);color:var(--white);font-size:12px;font-weight:700;letter-spacing:1px;border-radius:22px;padding:10px 10px 10px 22px;text-decoration:none}
.btn-arrow{width:24px;height:24px;border-radius:50%;border:1.5px solid var(--white);display:flex;align-items:center;justify-content:center}
.hero .btn{position:absolute;left:60px;top:198px}
.hero-image{position:absolute;left:0;top:260px;width:1200px;height:370px;background:linear-gradient(180deg,#d8d0c0 0%,#a99a7c 45%,#7a6c52 100%)}

/* about */
.about{position:absolute;top:720px;left:0;width:1200px;height:460px}
.eyebrow{font-size:12px;color:var(--gold);letter-spacing:.5px}
.about .eyebrow{position:absolute;left:112px;top:72px}
.about h2{position:absolute;left:112px;top:92px;font-family:"Cinzel",Georgia,serif;font-size:34px;font-weight:600;color:var(--navy)}
.about-text{position:absolute;left:112px;top:152px;width:600px;font-size:12px;line-height:19px;color:var(--muted)}
.about-text p+p{margin-top:12px}
.about-text strong{color:var(--ink)}
.pillars{position:absolute;left:112px;top:322px;display:flex;gap:24px}
.pillar{width:82px;text-align:center}
.pillar-icon{width:68px;height:68px;border-radius:50%;border:2px solid var(--gold);margin:0 auto 10px;display:flex;align-items:center;justify-content:center}
.pillar span{font-family:"Cinzel",Georgia,serif;font-size:13px;font-weight:700;color:var(--navy)}
.about-shade{position:absolute;left:0;bottom:0;width:1200px;height:14px;background:linear-gradient(180deg,rgba(0,0,0,.07),rgba(0,0,0,0))}

/* investment areas */
.areas{position:absolute;top:1180px;left:0;width:1200px;height:1580px}
.section-head{text-align:center}
.areas .section-head{position:absolute;top:118px;width:1200px}
.section-head h2{font-family:"Cinzel",Georgia,serif;font-size:34px;font-weight:600;color:var(--navy);margin-top:4px}
.area{position:absolute;left:112px;width:976px;height:146px;display:flex;align-items:center}
.area::after{content:"";position:absolute;left:0;right:0;bottom:-24px;height:1px;background:var(--line)}
.area-photo{width:220px;height:146px;flex:none}
.area-body{margin-left:60px;width:500px}
.area-body h3{font-family:"Cinzel",Georgia,serif;font-size:22px;font-weight:600;color:var(--gold)}
.area-body p{font-size:12px;line-height:18px;color:var(--muted);margin-top:10px}
.area-link{margin-left:auto;width:44px;height:44px;border-radius:50%;border:1.5px solid var(--navy);display:flex;align-items:center;justify-content:center}
.area-link.is-active{background:var(--gold);border-color:var(--gold)}

/* social responsibility */
.social{position:absolute;top:2760px;left:0;width:1200px;height:340px;background:var(--navy)}
.social-photo{position:absolute;left:0;top:0;width:700px;height:340px;background:linear-gradient(90deg,#c9a27e 0%,#8a6a52 55%,#2d3443 100%)}
.social-copy{position:absolute;left:764px;top:88px;width:380px;color:var(--white)}
.social-copy .eyebrow{color:var(--gold-soft)}
.social-copy h2{font-family:"Cinzel",Georgia,serif;font-size:30px;font-weight:600;line-height:34px;margin-top:4px}
.social-copy p{font-size:11px;line-height:17px;color:#c8ccd4;margin-top:12px}
.social-copy .btn{margin-top:16px}

/* contact */
.contact{position:absolute;top:3100px;left:0;width:1200px;height:560px}
.contact .section-head{position:absolute;top:80px;width:1200px}
.contact-intro{width:520px;margin:8px auto 0;font-size:12px;line-height:18px;color:var(--muted)}
.contact-form{position:absolute;left:180px;top:260px;width:580px}
.field-row{display:flex;gap:40px;margin-bottom:22px}
.field{flex:1}
.field label{display:block;font-size:11px;color:var(--muted);margin-bottom:14px}
.field .input{height:1px;background:#bcbcbc}
.field.tall .input{margin-top:50px}
.contact-form .btn{margin-top:10px}
.contact-info{position:absolute;left:820px;top:260px;width:260px}
.info-item{display:flex;gap:14px;align-items:flex-start;margin-bottom:26px}
.info-icon{width:36px;height:36px;border-radius:50%;background:var(--gold);flex:none;display:flex;align-items:center;justify-content:center}
.info-item p{font-size:12px;line-height:17px;color:var(--ink)}
.info-item p strong{font-weight:700}

/* footer */
.site-footer{position:absolute;top:3660px;left:0;width:1200px;height:200px;background:var(--navy-deep)}
.footer-brand{position:absolute;left:60px;top:70px;display:flex;flex-direction:column;align-items:center;gap:8px}
.footer-brand .brand-dot{width:44px;height:44px}
.footer-brand .brand-name{font-size:17px}
.footer-nav{position:absolute;left:0;top:82px;width:1200px;text-align:center}
.footer-nav a{font-size:11px;color:#c8ccd4;text-decoration:none;margin:0 8px}
.footer-nav p{font-size:10px;color:#8b93a1;margin-top:10px}
.social-links{position:absolute;right:80px;top:80px;display:flex;gap:10px}
.social-links span{width:30px;height:30px;border-radius:50%;border:1px solid var(--gold)}
</style>
</head>
<body>

<header class="site-header">
  <div class="brand"><span class="brand-dot"></span><span class="brand-name">R. T. HOLLOWAY</span></div>
  <nav class="main-nav">
    <a href="#" class="is-active">HOME</a>
    <a href="#">INVESTMENT AREA</a>
    <a href="#">SOCIAL RESPONSIBILITY</a>
    <a href="#">CONTACT US</a>
  </nav>
  <div class="call">
    <span class="call-icon"><svg width="14" height="14" viewBox="0 0 24 24" fill="#fff"><path d="M6.6 10.8a15 15 0 0 0 6.6 6.6l2.2-2.2c.3-.3.7-.4 1-.2 1.1.4 2.3.6 3.6.6.6 0 1 .4 1 1V20c0 .6-.4 1-1 1C10.6 21 3 13.4 3 4c0-.6.4-1 1-1h3.5c.6 0 1 .4 1 1 0 1.3.2 2.5.6 3.6.1.3 0 .7-.2 1z"/></svg></span>
    <div><small>Call us on</small><strong>+1 (000) 000 0000</strong></div>
  </div>
</header>

<section class="hero">
  <h1>WELCOME TO R. T. HOLLOWAY, INC.</h1>
  <p>R. T. Holloway, Inc. helps develop into a great nation and, with assertiveness, startup its footprint worldwide.</p>
  <a href="#" class="btn">GET STARTED <span class="btn-arrow"><svg width="12" height="12" viewBox="0 0 12 12"><path d="M2 6h8M7 3l3 3-3 3" stroke="#fff" stroke-width="1.5" fill="none"/></svg></span></a>
  <div class="hero-image" role="img" aria-label="Gold-toned city skyline with high-rise towers"></div>
</section>

<section class="about">
  <span class="eyebrow">About Us</span>
  <h2>R. T. Holloway</h2>
  <div class="about-text">
    <p>Based in Houston, Texas, R. T. Holloway, Inc. is an investment company founded in 2015 with the purpose of active assistance for socio-economic development and market platforms for harnessing the potential of world resources, designed to meet the demands of the emerging markets. R. T. Holloway, Inc. focuses on activities that enable investment.</p>
    <p>R. T. Holloway, Inc. holds interests in assets &amp; investments that are tied to the international economy:<br><strong>Sectors of Energy, Mining, Industry, Finance and Real Estate</strong></p>
  </div>
  <div class="pillars">
    <div class="pillar"><div class="pillar-icon"><svg width="34" height="34" viewBox="0 0 34 34" fill="none" stroke="#b3955a" stroke-width="2"><circle cx="17" cy="17" r="13"/><circle cx="17" cy="17" r="7"/><circle cx="17" cy="17" r="2" fill="#b3955a"/></svg></div><span>Mission</span></div>
    <div class="pillar"><div class="pillar-icon"><svg width="36" height="24" viewBox="0 0 36 24" fill="none" stroke="#b3955a" stroke-width="2"><path d="M2 12C8 3 28 3 34 12 28 21 8 21 2 12z"/><circle cx="18" cy="12" r="5"/></svg></div><span>Vision</span></div>
    <div class="pillar"><div class="pillar-icon"><svg width="34" height="30" viewBox="0 0 34 30" fill="none" stroke="#b3955a" stroke-width="2"><path d="M8 2h18l6 8-15 18L2 10z"/><path d="M2 10h30"/></svg></div><span>Value</span></div>
    <div class="pillar"><div class="pillar-icon"><svg width="36" height="30" viewBox="0 0 36 30" fill="none" stroke="#b3955a" stroke-width="2"><circle cx="18" cy="9" r="5"/><path d="M8 28c0-6 4-10 10-10s10 4 10 10"/><circle cx="6" cy="12" r="3"/><circle cx="30" cy="12" r="3"/></svg></div><span>Leadership</span></div>
  </div>
  <div class="about-shade"></div>
</section>

<section class="areas">
  <div class="section-head"><span class="eyebrow">What We Do</span><h2>Investment Areas</h2></div>

  <article class="area" style="top:260px">
    <div class="area-photo" role="img" aria-label="Solar panels and wind turbine at sunset" style="background:linear-gradient(160deg,#f2c27a,#8a7a6a 60%,#3e5570)"></div>
    <div class="area-body"><h3>Energy</h3><p>R. T. Holloway, Inc. holds investment stock in Exploration &amp; Production, and support field services for Gulf producers.</p></div>
    <span class="area-link is-active"><svg width="16" height="16" viewBox="0 0 16 16"><path d="M2 8h11M9 4l4 4-4 4" stroke="#1f2a3a" stroke-width="1.6" fill="none"/></svg></span>
  </article>

  <article class="area" style="top:454px">
    <div class="area-photo" role="img" aria-label="Open-pit mine with heavy trucks" style="background:linear-gradient(160deg,#e2a970,#a7714a 55%,#6d4a33)"></div>
    <div class="area-body"><h3>Mining</h3><p>R. T. Holloway, Inc. holds interests in the management &amp; operations of diamond mines, with annual production of 12,000 ct.</p></div>
    <span class="area-link"><svg width="16" height="16" viewBox="0 0 16 16"><path d="M2 8h11M9 4l4 4-4 4" stroke="#1f2a3a" stroke-width="1.6" fill="none"/></svg></span>
  </article>

  <article class="area" style="top:648px">
    <div class="area-photo" role="img" aria-label="Industrial plant with chimneys under blue sky" style="background:linear-gradient(160deg,#9ec3e6,#6d8fb3 55%,#b08a5c)"></div>
    <div class="area-body"><h3>Industry</h3><p>R. T. Holloway, Inc. holds investments in modern manufacturing plants with four warehouses in Texas, Louisiana and Georgia.</p></div>
    <span class="area-link"><svg width="16" height="16" viewBox="0 0 16 16"><path d="M2 8h11M9 4l4 4-4 4" stroke="#1f2a3a" stroke-width="1.6" fill="none"/></svg></span>
  </article>

  <article class="area" style="top:842px">
    <div class="area-photo" role="img" aria-label="Financial charts and calculator on a desk" style="background:linear-gradient(160deg,#e6e6ea,#b9c0cc 55%,#c07a5a)"></div>
    <div class="area-body"><h3>Finance</h3><p>R. T. Holloway, Inc. serves as a platform for regional foreign investment that target sectors include Oil &amp; Gas, Minerals, Mining.</p></div>
    <span class="area-link"><svg width="16" height="16" viewBox="0 0 16 16"><path d="M2 8h11M9 4l4 4-4 4" stroke="#1f2a3a" stroke-width="1.6" fill="none"/></svg></span>
  </article>

  <article class="area" style="top:1036px">
    <div class="area-photo" role="img" aria-label="Doctor attending a patient in a clinic" style="background:linear-gradient(160deg,#dfe6ee,#9fb2c7 55%,#4d6580)"></div>
    <div class="area-body"><h3>Healthcare</h3><p>R. T. Holloway, Inc. is committed to develop an investment project in a health care unit, with a diversified offer of service in specialties.</p></div>
    <span class="area-link"><svg width="16" height="16" viewBox="0 0 16 16"><path d="M2 8h11M9 4l4 4-4 4" stroke="#1f2a3a" stroke-width="1.6" fill="none"/></svg></span>
  </article>

  <article class="area" style="top:1230px">
    <div class="area-photo" role="img" aria-label="Modern two-storey residential house" style="background:linear-gradient(160deg,#eef1f4,#c9a58a 55%,#8a5e45)"></div>
    <div class="area-body"><h3>Real Estate</h3><p>R. T. Holloway, Inc. We have in our portfolio the following projects.</p></div>
    <span class="area-link"><svg width="16" height="16" viewBox="0 0 16 16"><path d="M2 8h11M9 4l4 4-4 4" stroke="#1f2a3a" stroke-width="1.6" fill="none"/></svg></span>
  </article>
</section>

<section class="social">
  <div class="social-photo" role="img" aria-label="Two women working together at a laptop"></div>
  <div class="social-copy">
    <span class="eyebrow">Why Us</span>
    <h2>Social<br>Responsibility</h2>
    <p>Since the commencement of our activity, R. T. Holloway, Inc. contributes to change the quality of life of children and seniors across the world providing them with support for primary and secondary basic needs so they can believe in the kindness of every human being.</p>
    <a href="#" class="btn">LEARN MORE <span class="btn-arrow"><svg width="12" height="12" viewBox="0 0 12 12"><path d="M2 6h8M7 3l3 3-3 3" stroke="#fff" stroke-width="1.5" fill="none"/></svg></span></a>
  </div>
</section>

<section class="contact">
  <div class="section-head">
    <span class="eyebrow">Get in Touch</span>
    <h2>Contact Us</h2>
    <p class="contact-intro">Get in touch with our talented team and start your journey to expanding your company and meeting your business bosses more agile and profitable.</p>
  </div>
  <form class="contact-form">
    <div class="field-row"><div class="field"><label>Name *</label><div class="input"></div></div><div class="field"><label>Email *</label><div class="input"></div></div></div>
    <div class="field-row"><div class="field"><label>Phone *</label><div class="input"></div></div><div class="field"><label>Service *</label><div class="input"></div></div></div>
    <div class="field-row"><div class="field tall"><label>Message *</label><div class="input"></div></div></div>
    <a href="#" class="btn">SUBMIT <span class="btn-arrow"><svg width="12" height="12" viewBox="0 0 12 12"><path d="M2 6h8M7 3l3 3-3 3" stroke="#fff" stroke-width="1.5" fill="none"/></svg></span></a>
  </form>
  <div class="contact-info">
    <div class="info-item"><span class="info-icon"><svg width="14" height="16" viewBox="0 0 14 18" fill="#fff"><path d="M7 0a7 7 0 0 0-7 7c0 5 7 11 7 11s7-6 7-11a7 7 0 0 0-7-7zm0 9.5A2.5 2.5 0 1 1 7 4.5a2.5 2.5 0 0 1 0 5z"/></svg></span><p><strong>R. T. HOLLOWAY, INC</strong><br>3870 Oak Ridge Lane,<br>Houston, TX 77002</p></div>
    <div class="info-item"><span class="info-icon"><svg width="14" height="14" viewBox="0 0 24 24" fill="#fff"><path d="M6.6 10.8a15 15 0 0 0 6.6 6.6l2.2-2.2c.3-.3.7-.4 1-.2 1.1.4 2.3.6 3.6.6.6 0 1 .4 1 1V20c0 .6-.4 1-1 1C10.6 21 3 13.4 3 4c0-.6.4-1 1-1h3.5c.6 0 1 .4 1 1 0 1.3.2 2.5.6 3.6.1.3 0 .7-.2 1z"/></svg></span><p><strong>+1 (000) 000 0000</strong></p></div>
    <div class="info-item"><span class="info-icon"><svg width="16" height="12" viewBox="0 0 16 12" fill="none" stroke="#fff" stroke-width="1.5"><rect x="1" y="1" width="14" height="10"/><path d="M1 1l7 6 7-6"/></svg></span><p><strong>name@rtholloway.com</strong></p></div>
  </div>
</section>

<footer class="site-footer">
  <div class="footer-brand"><span class="brand-dot"></span><span class="brand-name">R. T. HOLLOWAY</span></div>
  <div class="footer-nav">
    <a href="#">Home</a>|<a href="#">About Us</a>|<a href="#">Investment Areas</a>|<a href="#">Social Responsibility</a>|<a href="#">Contact Us</a>
    <p>&copy; R. T. HOLLOWAY, INC. 2023. All rights reserved.</p>
  </div>
  <div class="social-links"><span></span><span></span><span></span></div>
</footer>

</body>
</html>
```